Dorsey K. Whitfield Business Card

We need a business card for our company Dorsey K. Whitfield Heating & Plumbing to be distributed to potential customers. It should follow the color scheme of our logo and have a modern upscale and masculine look.

The logo is attached and the info below should also be included:

5187 W. Quarry Bend Rd.
Brookhollow, PA 17688

Tobias R. Whitfield
(717) 593-8126
tobiasreedwhitfield@mailvane.com
dorseykwhitfield.com
PA #038419

Industry/Entity Type

Business

Contact Information for Business Card

5187 W. Quarry Bend Rd.
Brookhollow, PA 17688

Tobias R. Whitfield
(717) 593-8126
tobiasreedwhitfield@mailvane.com
dorseykwhitfield.com
PA #038419

Colors

Designer to choose colors to be used in the design.

Requirements
Must have
• Information above included

```html
<!DOCTYPE html>
<html lang="en">
<head>
<meta charset="utf-8">
<title>Dorsey K. Whitfield Heating &amp; Plumbing — Business Card</title>
<link rel="stylesheet" href="https://fonts.googleapis.com/css2?family=Archivo:wght@800&family=Open+Sans:wght@400;600&display=swap">
<style>
  :root {
    --stage: #ecebe8;
    --lime: #abd037;
    --brand-blue: #0a56a5;
    --ink: #2a2a2a;
    --paper: #ffffff;
    --rule: #abd037;
  }
  * { box-sizing: border-box; margin: 0; padding: 0; }
  html, body { width: 1200px; height: 880px; overflow: hidden; }
  body {
    background: var(--stage);
    font-family: "Open Sans", Arial, sans-serif;
    color: var(--ink);
    position: relative;
  }
  .card {
    position: absolute;
    left: 250px;
    width: 700px;
    height: 400px;
    box-shadow: 0 2px 10px rgba(0,0,0,0.12);
  }
  /* Front */
  .card-front { top: 30px; background: var(--lime); }
  .front-brand {
    position: absolute;
    left: 0; right: 0; top: 130px;
    display: flex; align-items: center; justify-content: center; gap: 22px;
  }
  .brand-square {
    width: 64px; height: 64px;
    background: var(--brand-blue);
    flex: none;
  }
  .brand-name {
    font-family: "Archivo", "Arial Black", sans-serif;
    font-weight: 800;
    color: var(--brand-blue);
    line-height: 1.05;
  }
  .front-brand .brand-name { font-size: 40px; }
  .front-web {
    position: absolute;
    left: 0; right: 0; top: 300px;
    text-align: center;
    font-size: 17px;
    letter-spacing: 4px;
    color: var(--ink);
  }
  /* Back */
  .card-back { top: 450px; background: var(--paper); }
  .back-brand {
    position: absolute;
    left: 40px; top: 48px;
    display: flex; align-items: center; gap: 16px;
  }
  .back-brand .brand-square { width: 56px; height: 56px; }
  .back-brand .brand-name { font-size: 26px; }
  .back-rule {
    position: absolute;
    left: 112px; top: 128px;
    width: 300px; height: 2px;
    background: var(--rule);
  }
  .holder-name {
    position: absolute;
    right: 48px; top: 72px;
    font-family: "Archivo", "Arial Black", sans-serif;
    font-weight: 800;
    font-size: 20px;
    color: var(--brand-blue);
    text-transform: uppercase;
    letter-spacing: 0.5px;
  }
  .contact-list {
    position: absolute;
    left: 160px; top: 190px;
    list-style: none;
    font-size: 19px;
    line-height: 32px;
  }
  .contact-list li { display: flex; align-items: center; gap: 10px; }
  .contact-icon { width: 18px; height: 18px; flex: none; }
  .contact-list .licence { padding-left: 28px; }
  .address {
    position: absolute;
    left: 188px; top: 336px;
    font-size: 19px;
  }
</style>
</head>
<body>

<section class="card card-front" aria-label="Card front">
  <div class="front-brand">
    <span class="brand-square" aria-hidden="true"></span>
    <span class="brand-name">Dorsey K. Whitfield</span>
  </div>
  <p class="front-web">www.dorseykwhitfield.com</p>
</section>

<section class="card card-back" aria-label="Card back">
  <div class="back-brand">
    <span class="brand-square" aria-hidden="true"></span>
    <span class="brand-name">Dorsey K. Whitfield<br>Heating &amp; Plumbing</span>
  </div>
  <span class="back-rule" aria-hidden="true"></span>

  <p class="holder-name">Tobias R. Whitfield</p>

  <ul class="contact-list">
    <li>
      <svg class="contact-icon" viewBox="0 0 18 18" aria-hidden="true">
        <circle cx="9" cy="9" r="8" fill="none" stroke="#abd037" stroke-width="1.6"/>
        <path d="M6.5 5 L8 5 L8.6 7 L7.6 7.8 Q8.4 9.8 10.2 10.6 L11 9.6 L13 10.2 L13 11.6 Q9.5 12.5 7 9.8 Q5.2 7.6 6.5 5 Z" fill="#abd037"/>
      </svg>
      (717) 593-8126
    </li>
    <li>
      <svg class="contact-icon" viewBox="0 0 18 18" aria-hidden="true">
        <rect x="1.5" y="4" width="15" height="10.5" rx="1" fill="#abd037"/>
        <path d="M2 4.8 L9 10 L16 4.8" fill="none" stroke="#fff" stroke-width="1.4"/>
      </svg>
      tobiasreedwhitfield@mailvane.com
    </li>
    <li>
      <svg class="contact-icon" viewBox="0 0 18 18" aria-hidden="true">
        <g fill="none" stroke="#abd037" stroke-width="1.4">
          <circle cx="9" cy="9" r="7.5"/>
          <ellipse cx="9" cy="9" rx="3.3" ry="7.5"/>
          <line x1="1.5" y1="9" x2="16.5" y2="9"/>
          <line x1="2.8" y1="5" x2="15.2" y2="5"/>
          <line x1="2.8" y1="13" x2="15.2" y2="13"/>
        </g>
      </svg>
      www.dorseykwhitfield.com
    </li>
    <li class="licence">PA #038419</li>
  </ul>

  <p class="address">5187 W. Quarry Bend Rd., Brookhollow, PA 17688</p>
</section>

</body>
</html>
```